Business card design

Hi,
I need to have a business card design based on the current logo.
If competitive I not put it out to everyone.

It can be single of double sided

Target Market(s)

Food businesses

Industry/Entity Type

Food Manufacturing

Contact Information for Business Card

Details will on card will be as follows Name = Marcus Helt Email = Marcus@TalBakery.com.au Phone = 0418562207 Address = 17 Lanford Street , Marlow Heights QLD 4127 Australia

Font styles to use
Other font styles liked:
• based on two fonts - Adelle & Museo

Requirements
Must have
• Based on the on switch concept

```html
<!DOCTYPE html>
<html lang="en">
<head>
<meta charset="utf-8">
<title>TalBakery Business Card</title>
<link rel="stylesheet" href="https://fonts.googleapis.com/css2?family=Arimo:wght@400;700&family=Zilla+Slab:wght@500&display=swap">
<style>
  :root {
    --page: #2b2b2d;
    --card-dark: #3d2a2c;
    --brand-pink: #ec2a4b;
    --paper: #ffffff;
    --ink-light: #ffffff;
    --ink-dark: #3d2a2c;
  }
  * { box-sizing: border-box; margin: 0; padding: 0; }
  html, body { width: 1200px; height: 1015px; overflow: hidden; }
  body {
    background: var(--page);
    font-family: "Arimo", Arial, sans-serif;
    position: relative;
  }
  .card {
    position: absolute;
    left: 320px;
    width: 560px;
    height: 320px;
    background: var(--card-dark);
    overflow: hidden;
    box-shadow: 0 12px 30px rgba(0,0,0,.45);
  }
  .card--front { top: 150px; }
  .card--back { top: 545px; }

  .brand { display: flex; align-items: center; gap: 12px; }
  .brand__dot {
    width: 34px; height: 34px; border-radius: 50%;
    background: var(--brand-pink); flex: none;
  }
  .brand__name {
    font-weight: 700; font-size: 56px; letter-spacing: 2px; line-height: 1;
  }
  .card--front .brand {
    position: absolute; left: 112px; top: 110px;
  }
  .card--front .brand__name { color: var(--ink-light); }
  .brand__tagline {
    position: absolute; left: 158px; top: 176px;
    font-family: "Zilla Slab", Georgia, serif; font-weight: 500;
    font-size: 17px; color: var(--ink-light); letter-spacing: .5px;
  }

  .card__backdrop { position: absolute; inset: 0; }
  .card--back .brand {
    position: absolute; left: 318px; top: 122px; gap: 10px;
  }
  .card--back .brand__dot { width: 22px; height: 22px; }
  .card--back .brand__name { color: var(--ink-dark); font-size: 32px; letter-spacing: 1px; }

  .holder {
    position: absolute; left: 36px; top: 54px;
    color: var(--brand-pink); font-weight: 700; font-size: 24px; letter-spacing: 1.5px;
    text-transform: uppercase;
  }
  .address {
    position: absolute; left: 50px; top: 160px;
    color: var(--ink-light); font-size: 14px; line-height: 1.35;
  }
  .contact-list {
    position: absolute; left: 50px; top: 232px; list-style: none;
    color: var(--ink-light); font-size: 14px; line-height: 1.4;
  }
  .contact-list li { display: flex; align-items: center; gap: 8px; }
  .contact-list svg { width: 13px; height: 13px; flex: none; }
</style>
</head>
<body>

<section class="card card--front">
  <div class="brand">
    <span class="brand__dot"></span>
    <span class="brand__name">TalBakery</span>
  </div>
  <p class="brand__tagline">Fresh Bakes Every Morning</p>
</section>

<section class="card card--back">
  <svg class="card__backdrop" width="560" height="320" viewBox="0 0 560 320">
    <circle cx="470" cy="140" r="222" fill="#ffffff"/>
    <path d="M 290 30 A 205 205 0 0 0 440 330" fill="none" stroke="#ec2a4b" stroke-width="3"/>
  </svg>

  <div class="brand">
    <span class="brand__dot"></span>
    <span class="brand__name">TalBakery</span>
  </div>

  <h1 class="holder">Marcus Helt</h1>

  <p class="address">
    17 Lanford Street<br>
    Marlow Heights<br>
    QLD 4127 Australia
  </p>

  <ul class="contact-list">
    <li>
      <svg viewBox="0 0 24 24" aria-hidden="true"><path fill="#ec2a4b" d="M6.6 10.8a15 15 0 0 0 6.6 6.6l2.2-2.2a1 1 0 0 1 1-.25 11.4 11.4 0 0 0 3.6.57 1 1 0 0 1 1 1V20a1 1 0 0 1-1 1A17 17 0 0 1 3 4a1 1 0 0 1 1-1h3.5a1 1 0 0 1 1 1c0 1.25.2 2.45.57 3.570a1 1 0 0 1-.25 1z"/></svg>
      0418562207
    </li>
    <li>
      <svg viewBox="0 0 24 24" aria-hidden="true"><path fill="#ec2a4b" d="M2 5h20v14H2z"/><path fill="none" stroke="#3d2a2c" stroke-width="1.6" d="M2 5l10 8 10-8"/></svg>
      Marcus@TalBakery.com.au
    </li>
    <li>
      <svg viewBox="0 0 24 24" aria-hidden="true"><g fill="none" stroke="#ec2a4b" stroke-width="2"><circle cx="12" cy="12" r="9"/><path d="M3 12h18M12 3c3 3 3 15 0 18M12 3c-3 3-3 15 0 18"/></g></svg>
      www.TalBakery.com.au
    </li>
  </ul>
</section>

</body>
</html>
```